Catering Box for Food

We run a restaurant business called "Zembrix"
www.zembrix-eats.example
We're expanding into catering services and are currently designing a new delivery box.
---Box Concept
The food will be packed in a full-size aluminum tray.
The tray will be placed inside a white paper box for delivery and branding purposes.(as the pics showed )
Box dimensions: 21 x 13 x 4 inches
Brand color: HEX #FF6C0E
The design should use no more than two colors (not including white).
---Design Requirements Please create a design for all five visible surfaces of the box:
Top
Front
Back
Left side
Right side
---Additional Info
The box should also include our store locations, with addresses and phone numbers clearly displayed.

```html
<!DOCTYPE html>
<html lang="en">
<head>
<meta charset="utf-8">
<title>Zembrix Catering Box – Flat Layout</title>
<link rel="stylesheet" href="https://fonts.googleapis.com/css2?family=Lato:ital,wght@0,300;0,400;0,700;0,900;1,400;1,700&display=swap">
<style>
  :root {
    --brand-orange: #F07022;
    --band-orange: #E0631F;
    --pattern-cream: #FCEFE4;
    --paper-white: #FFFFFF;
    --ink: #2B2B2B;
    --backdrop: #A3A3A0;
    --fold-line: #C9C9C6;
  }
  * { box-sizing: border-box; margin: 0; padding: 0; }
  html, body { width: 1200px; height: 803px; overflow: hidden; }
  body {
    background: var(--backdrop);
    font-family: "Lato", sans-serif;
    position: relative;
  }
  .panel {
    position: absolute;
    background: var(--paper-white);
    outline: 1px solid var(--fold-line);
    overflow: hidden;
  }
  .panel--back  { left: 243px; top: 44px;  width: 714px; height: 136px; }
  .panel--top   { left: 243px; top: 180px; width: 714px; height: 442px; }
  .panel--front { left: 243px; top: 622px; width: 714px; height: 136px; }
  .panel--left  { left: 107px; top: 180px; width: 136px; height: 442px; }
  .panel--right { left: 957px; top: 180px; width: 136px; height: 442px; }

  /* Top lid */
  .lid-pattern {
    position: absolute; inset: 0;
    background: radial-gradient(ellipse at center, var(--paper-white) 0%, var(--pattern-cream) 100%);
  }
  .lid-brand {
    position: absolute; left: 0; right: 0; top: 150px;
    text-align: center;
  }
  .brand-name {
    color: var(--brand-orange);
    font-weight: 900;
    font-size: 92px;
    line-height: 1;
    letter-spacing: 1px;
  }
  .brand-tagline {
    color: var(--brand-orange);
    font-weight: 900;
    font-size: 24px;
    letter-spacing: 2px;
    margin-top: 8px;
  }
  .lid-url {
    position: absolute; left: 0; right: 0; bottom: 44px;
    text-align: center;
    font-weight: 300;
    font-size: 26px;
    color: var(--ink);
  }

  /* Front */
  .front-mark {
    position: absolute; left: 0; right: 0; top: 14px;
    text-align: center;
    color: var(--brand-orange);
    font-weight: 900;
    font-size: 26px;
  }
  .front-band {
    position: absolute; left: 0; right: 0; bottom: 0; height: 70px;
    background: var(--band-orange);
    display: flex; align-items: center; justify-content: center;
  }
  .front-band__text {
    color: var(--paper-white);
    font-weight: 700;
    font-style: italic;
    font-size: 30px;
    letter-spacing: 5px;
  }

  /* Back */
  .back-rule {
    position: absolute; left: 24px; right: 24px; height: 1px;
    background: var(--brand-orange);
  }
  .back-rule--upper { top: 16px; }
  .back-rule--lower { bottom: 16px; }
  .back-mark {
    position: absolute; left: 36px; top: 40px;
    display: flex; align-items: center; gap: 10px;
  }
  .back-mark__dot {
    width: 56px; height: 56px; border-radius: 50%;
    background: var(--brand-orange);
    flex: none;
  }
  .back-mark__name {
    color: var(--brand-orange);
    font-weight: 900;
    font-size: 22px;
    white-space: nowrap;
  }
  .locations {
    position: absolute; left: 262px; right: 28px; top: 34px;
    display: flex; justify-content: space-between;
    font-size: 12px; line-height: 1.4; color: var(--ink);
    white-space: nowrap;
  }
  .location__city { font-weight: 700; }
  .order-online__label { font-weight: 700; font-style: italic; }
  .order-online__url { color: var(--brand-orange); font-weight: 700; font-size: 13px; }

  /* Sides */
  .side-content {
    position: absolute; left: 50%; top: 50%;
    width: 442px; height: 136px;
    transform: translate(-50%, -50%) rotate(90deg);
    display: flex; align-items: center; justify-content: center; gap: 16px;
  }
  .panel--left .side-content { transform: translate(-50%, -50%) rotate(-90deg); }
  .side-mark__dot {
    width: 46px; height: 46px; border-radius: 50%;
    background: var(--brand-orange);
  }
  .side-slogan {
    font-weight: 700;
    font-size: 15px;
    letter-spacing: 2px;
    color: var(--ink);
  }
</style>
</head>
<body>

  <section class="panel panel--back" aria-label="Back panel">
    <div class="back-rule back-rule--upper"></div>
    <div class="back-mark">
      <div class="back-mark__dot"></div>
      <span class="back-mark__name">Zembrix</span>
    </div>
    <div class="locations">
      <div class="location">
        <div class="location__city">Alder Park</div>
        <div>410 Harlow Ave,</div>
        <div>Alder Park, CA 90000</div>
        <div>(555) 014-2287</div>
      </div>
      <div class="location">
        <div class="location__city">Westmere</div>
        <div>88 Linden Row,</div>
        <div>Westmere, CA 90000</div>
        <div>(555) 019-6630</div>
      </div>
      <div class="order-online">
        <div class="order-online__label">Order Online:</div>
        <div class="order-online__url">www.zembrix-eats.example</div>
      </div>
    </div>
    <div class="back-rule back-rule--lower"></div>
  </section>

  <section class="panel panel--left" aria-label="Left side panel">
    <div class="side-content">
      <div class="side-mark__dot"></div>
      <span class="side-slogan">FRESH. AUTHENTIC. TO GO.</span>
    </div>
  </section>

  <section class="panel panel--top" aria-label="Top lid">
    <div class="lid-pattern" role="img" aria-label="Faint repeating pattern of outlined hen silhouettes in pale orange"></div>
    <div class="lid-brand">
      <div class="brand-name">Zembrix</div>
      <div class="brand-tagline">HAINAN CHICKEN</div>
    </div>
    <div class="lid-url">www.zembrix-eats.example</div>
  </section>

  <section class="panel panel--right" aria-label="Right side panel">
    <div class="side-content">
      <div class="side-mark__dot"></div>
      <span class="side-slogan">FRESH. AUTHENTIC. TO GO.</span>
    </div>
  </section>

  <section class="panel panel--front" aria-label="Front panel">
    <div class="front-mark">Zembrix</div>
    <div class="front-band">
      <span class="front-band__text">Hainan Chicken Catering</span>
    </div>
  </section>

</body>
</html>
```